Modern Homepage Design for brenvik.nl – Fish & Chicken Food Webshop

Brenvik.nl is an online store that sells fish and chicken food. The design should be visually appealing, easy to navigate, and optimized for e-commerce. We want a layout that helps customers quickly find what they need and encourages them to explore our products.
A good example of the style and structure we like is dierkamp.nl – clean layout, clear product focus, and user-friendly navigation.
Brand Colors (must be used):
Orange: #f7a441
Dark Gray: #3c3c3b
White: #ffffff
Please use these colors consistently throughout the design.
Homepage Requirements:
The homepage should include the following sections:
Main Slider / Hero Banner
A large, eye-catching slider at the top of the page to highlight promotions or featured categories.
Category Blocks
A section with clear, clickable blocks or tiles that link to main product categories (e.g., Fish Food, Chicken Food, Accessories).
Featured Products
A section showcasing selected or best-selling products.
Special Offers / Promotions
A space to highlight current deals or limited-time offers.
Three Banners in a Row
A section with three horizontal banners side by side, which can be used for promotions, shipping info, or other key messages.
Unique Selling Points (USPs)
A section that briefly explains what makes our store different (e.g., fast delivery, high-quality feed, trusted by professionals).
SEO Content Block
A short paragraph of text for SEO purposes (use Lorem Ipsum for dummy content).
Footer Design
Include space for contact information, navigation links, and social media.
Design Notes:
The design must be responsive and mobile-friendly.
Focus on clean layout, good spacing, and easy navigation.
Use modern fonts and a clear visual hierarchy.
We are only looking for the homepage design at this stage, but we may work with the selected designer on additional pages later.
Deliverables:
Homepage design in layered PSD, Figma, or Adobe XD format
Any fonts and assets used
Preview images/mockups
We look forward to seeing your ideas and working with a designer who can bring our brand to life with a fresh and functional homepage design.
Let us know if you have any questions.
Hobby Animal Keepers, Pet Owners
Animal Nutrition & Feed
2 page

```html
<!DOCTYPE html>
<html lang="en">
<head>
<meta charset="UTF-8">
<title>Brenvik.nl – Fish &amp; Chicken Food</title>
<link href="https://fonts.googleapis.com/css2?family=Fredoka:wght@500;600;700&family=Poppins:wght@400;500;600;700&display=swap" rel="stylesheet">
<style>
:root{
  --orange:#f7a441;
  --dark:#3c3c3b;
  --white:#ffffff;
  --cream:#fbe8d3;
  --line:#2a4f8f;
  --border:#6d6d6d;
}
*{box-sizing:border-box;margin:0;padding:0}
a{text-decoration:none;color:inherit}
html,body{width:1200px;height:4012px;overflow:hidden;background:var(--white)}
body{position:relative;font-family:"Poppins",sans-serif;color:var(--dark)}

/* header */
.site-header{position:absolute;left:0;top:0;width:1200px;height:142px}
.brand{position:absolute;left:85px;top:44px;display:flex;align-items:center;gap:8px}
.brand-dot{width:34px;height:34px;border-radius:50%;background:var(--orange)}
.brand-name{font-family:"Fredoka",sans-serif;font-weight:600;font-size:40px;color:var(--dark);line-height:1}
.main-nav a{position:absolute;top:53px;font-weight:600;font-size:17px;color:var(--dark)}
.cart-btn{position:absolute;left:968px;top:47px;width:196px;height:40px;border-radius:20px;background:var(--orange);display:flex;align-items:center;padding-left:18px}

/* hero */
.hero-slide{position:absolute;left:0;width:1200px;overflow:hidden}
.hero-fish{top:142px;height:307px;background:
  radial-gradient(ellipse 260px 150px at 560px 100px,rgba(228,190,120,.85),rgba(228,190,120,0)),
  radial-gradient(ellipse 200px 140px at 800px 110px,rgba(236,214,70,.9),rgba(236,214,70,0)),
  radial-gradient(ellipse 240px 130px at 260px 250px,rgba(200,200,60,.55),rgba(200,200,60,0)),
  linear-gradient(110deg,#1f3f3a 0%,#2f5566 40%,#3d6a5a 70%,#1f3a2e 100%)}
.hero-chicken{top:449px;height:315px;background:
  radial-gradient(ellipse 220px 120px at 560px 250px,rgba(196,160,120,.95),rgba(196,160,120,0)),
  radial-gradient(ellipse 200px 200px at 440px 150px,rgba(170,60,30,.9),rgba(170,60,30,0)),
  radial-gradient(ellipse 240px 200px at 1000px 60px,rgba(230,190,140,.6),rgba(230,190,140,0)),
  linear-gradient(100deg,#3a1a10 0%,#6a2d18 35%,#8a5040 60%,#4a2c20 100%)}
.hero-btn{position:absolute;width:381px;height:142px;border-radius:38px;background:var(--orange);color:var(--white);font-family:"Fredoka",sans-serif;font-weight:700;font-size:32px;display:flex;align-items:center;justify-content:center}

/* section titles */
.section-title{position:absolute;left:0;width:1200px;text-align:center;font-family:"Fredoka",sans-serif;font-weight:700;font-size:45px;color:var(--orange)}

/* products */
.product{position:absolute;top:940px;width:240px;text-align:center}
.product-visual{position:relative;width:240px;height:235px}
.product-circle{position:absolute;left:23px;top:28px;width:206px;height:206px;border-radius:50%;background:var(--orange)}
.product-pack{position:absolute;left:68px;top:14px;width:118px;height:196px;border-radius:6px;box-shadow:0 4px 10px rgba(0,0,0,.15)}
.product-caption{font-size:13px;line-height:17px;margin-top:12px;padding:0 30px}
.stars{font-size:22px;color:var(--orange);letter-spacing:1px;line-height:1;margin-top:4px}
.stars .off{color:#cfcfcf}

/* promo */
.promo{position:absolute;left:159px;top:1386px;width:881px;height:209px;border-radius:40px;background:var(--orange);overflow:hidden}
.promo-art{position:absolute;left:0;top:0;width:230px;height:209px;background:
  radial-gradient(ellipse 80px 60px at 60px 150px,rgba(232,120,80,.9),rgba(232,120,80,0)),
  radial-gradient(ellipse 90px 70px at 150px 60px,rgba(70,140,190,.85),rgba(70,140,190,0)),
  linear-gradient(90deg,#d9c2a8 0%,#6f9ec0 55%,rgba(247,164,65,0) 100%)}
.promo-price{position:absolute;left:292px;top:16px;font-family:"Fredoka",sans-serif;font-weight:700;font-size:100px;color:var(--white);line-height:1}
.promo-text{position:absolute;left:292px;top:118px;font-size:21px;line-height:26px;color:var(--dark)}
.promo-small{position:absolute;left:292px;top:170px;font-size:11px;font-weight:600;color:var(--dark)}
.jar{position:absolute;border-radius:10px 10px 8px 8px}
.dots{position:absolute;left:507px;top:1614px;display:flex;gap:21px}
.dots span{width:19px;height:19px;border-radius:50%;border:2px solid var(--dark)}
.dots .on{background:var(--orange)}

/* three banners */
.tile{position:absolute;top:1783px;width:341px;height:173px;border-radius:16px;background:var(--orange)}
.tile-text{position:absolute;left:22px;top:32px;font-size:13px;line-height:17px;color:var(--dark)}
.tile-title{position:absolute;left:22px;top:90px;font-family:"Fredoka",sans-serif;font-weight:700;font-size:46px;color:var(--white);line-height:1}
.tile-art{position:absolute;top:-48px;left:178px;width:140px;height:200px;border-radius:60px}
.tile-arrow{position:absolute;right:14px;bottom:12px;width:40px;height:40px;border-radius:50%;background:var(--white);display:flex;align-items:center;justify-content:center}

/* USPs */
.usp{position:absolute;top:2218px;width:320px;text-align:center}
.usp-icon{width:124px;height:124px;border-radius:50%;background:var(--orange);margin:0 auto;display:flex;align-items:center;justify-content:center}
.usp-title{font-family:"Fredoka",sans-serif;font-weight:700;font-size:24px;margin-top:14px;line-height:1.2}
.usp-text{font-size:15px;line-height:21px;margin-top:4px}

/* SEO */
.seo-title{position:absolute;left:96px;top:2570px;font-family:"Fredoka",sans-serif;font-weight:700;font-size:30px}
.seo-text{position:absolute;left:96px;top:2634px;width:994px;font-size:15.5px;line-height:21px;text-align:justify}
.divider{position:absolute;left:199px;top:2818px;width:784px;height:2px;background:var(--line)}

/* form */
.field{position:absolute;width:406px}
.field label{display:block;font-size:16px;height:25px}
.field .input{height:53px;border:1.5px solid var(--border)}
.submit-btn{position:absolute;left:683px;top:3420px;width:406px;height:51px;background:var(--orange);color:var(--white);font-family:"Fredoka",sans-serif;font-weight:700;font-size:19px;letter-spacing:1px;display:flex;align-items:center;justify-content:center}

/* footer */
.site-footer{position:absolute;left:0;top:3622px;width:1200px;height:390px;background:var(--cream)}
.footer-col{position:absolute;top:120px}
.footer-col h4{font-family:"Fredoka",sans-serif;font-weight:700;font-size:19px;margin-bottom:14px}
.footer-col ul{list-style:none;font-size:13px;line-height:20px}
.footer-brand{position:absolute;left:866px;top:108px;display:flex;align-items:center;gap:10px}
.footer-brand .brand-dot{width:60px;height:60px}
.footer-brand .brand-name{font-size:68px}
.chat{position:absolute;left:864px;top:228px;width:90px;height:90px;border-radius:50%;background:#2fbf55;display:flex;align-items:center;justify-content:center}
.chat-badge{position:absolute;left:930px;top:226px;width:28px;height:28px;border-radius:50%;background:#e8322a;color:var(--white);font-size:14px;font-weight:600;display:flex;align-items:center;justify-content:center}
.chat-label{position:absolute;left:978px;top:246px;font-family:"Fredoka",sans-serif;font-weight:700;font-size:19px;line-height:22px}
</style>
</head>
<body>

<header class="site-header">
  <div class="brand"><span class="brand-dot"></span><span class="brand-name">Brenvik</span></div>
  <nav class="main-nav">
    <a href="#" style="left:422px">Fish Food</a>
    <a href="#" style="left:592px">Chicken Food</a>
    <a href="#" style="left:800px">Accessories</a>
  </nav>
  <a class="cart-btn" href="#" aria-label="Cart">
    <svg width="26" height="22" viewBox="0 0 26 22" fill="none" stroke="#fff" stroke-width="2.4" stroke-linecap="round" stroke-linejoin="round"><path d="M1 2h4l3 12h12l3-9H7"/><circle cx="10" cy="19" r="1.6" fill="#fff"/><circle cx="19" cy="19" r="1.6" fill="#fff"/></svg>
  </a>
</header>

<section class="hero-slide hero-fish" role="img" aria-label="Photo of colourful discus fish in an aquarium">
  <a class="hero-btn" href="#" style="left:83px;top:83px">Fish Food</a>
</section>
<section class="hero-slide hero-chicken" role="img" aria-label="Photo of a hen eating grain from a hand">
  <a class="hero-btn" href="#" style="left:767px;top:86px">Chicken Food</a>
</section>

<h2 class="section-title" style="top:826px">Best-Selling Products</h2>

<article class="product" style="left:64px">
  <div class="product-visual"><div class="product-circle"></div><div class="product-pack" role="img" aria-label="Pond fish food bag" style="background:linear-gradient(#2f6fc0 0%,#e9d05a 28%,#3a8ac8 45%,#c9a87a 80%,#3a7bc4 100%)"></div></div>
  <p class="product-caption">Sed ut perspiciatis unde sit voluptatem</p>
  <div class="stars">★★★★★</div>
</article>
<article class="product" style="left:337px">
  <div class="product-visual"><div class="product-circle"></div><div class="product-pack" role="img" aria-label="Layer feed sack" style="background:linear-gradient(#d8c9a4 0%,#b9a47c 40%,#8f7d5e 85%,#e8b64a 100%)"></div></div>
  <p class="product-caption">Sed ut perspiciatis unde sit voluptatem</p>
  <div class="stars">★★★★★</div>
</article>
<article class="product" style="left:611px">
  <div class="product-visual"><div class="product-circle"></div><div class="product-pack" role="img" aria-label="Koi pellet bag" style="background:linear-gradient(#c98a6a 0%,#b7866a 32%,#2a7ac0 40%,#1c4f8c 100%)"></div></div>
  <p class="product-caption">Sed ut perspiciatis unde sit voluptatem</p>
  <div class="stars">★★★★<span class="off">★</span></div>
</article>
<article class="product" style="left:895px">
  <div class="product-visual"><div class="product-circle"></div><div class="product-pack" role="img" aria-label="Organic chicken feed pouch" style="background:linear-gradient(#f4f1ec 0%,#ece6df 70%,#d8cfc4 100%);border-radius:14px"></div></div>
  <p class="product-caption">Sed ut perspiciatis unde sit voluptatem</p>
  <div class="stars">★★★★<span class="off">★</span></div>
</article>

<section class="promo">
  <div class="promo-art" role="img" aria-label="Illustration of a school of tropical fish"></div>
  <div class="promo-price">XX.-</div>
  <p class="promo-text">Sed ut perspiciatis<br>unde sit voluptatem</p>
  <p class="promo-small">ipsum huzhd</p>
</section>
<div role="img" aria-label="Stacked jars of aquarium fish food">
  <div class="jar" style="left:789px;top:1340px;width:76px;height:110px;background:linear-gradient(#e8c53a 0 14%,#d94a3a 14%,#c9603a 100%)"></div>
  <div class="jar" style="left:869px;top:1340px;width:76px;height:110px;background:linear-gradient(#8a5ad0 0 14%,#6a3aa8 14%,#7a4bb0 100%)"></div>
  <div class="jar" style="left:751px;top:1454px;width:76px;height:112px;background:linear-gradient(#2aa86a 0 14%,#1f7a4a 14%,#2a8a5a 100%)"></div>
  <div class="jar" style="left:832px;top:1454px;width:76px;height:112px;background:linear-gradient(#3a7ad8 0 14%,#1f3f8c 14%,#2a4fa0 100%)"></div>
  <div class="jar" style="left:913px;top:1454px;width:76px;height:112px;background:linear-gradient(#2aa86a 0 14%,#c04a3a 14%,#3a9a5a 100%)"></div>
</div>
<div class="dots"><span></span><span></span><span class="on"></span><span></span><span></span></div>

<a class="tile" href="#" style="left:59px">
  <p class="tile-text">Sed ut perspiciatis<br>unde sit voluptatem<br>kolu bjuzs</p>
  <div class="tile-title">SPER</div>
  <div class="tile-art" role="img" aria-label="Lionfish photo" style="background:linear-gradient(160deg,#f0e2d2,#d06a3a 60%,#8a3a1a)"></div>
  <span class="tile-arrow"><svg width="24" height="24" viewBox="0 0 24 24" fill="none" stroke="#222" stroke-width="2.6" stroke-linecap="round" stroke-linejoin="round"><path d="M4 12h16M13 5l7 7-7 7"/></svg></span>
</a>
<a class="tile" href="#" style="left:422px">
  <p class="tile-text">Sed ut perspiciatis<br>unde sit voluptatem<br>kolu bjuzs</p>
  <div class="tile-title">SPER</div>
  <div class="tile-art" role="img" aria-label="White hen photo" style="background:linear-gradient(160deg,#f6f4f1,#d6cfc6 70%,#e0a040)"></div>
  <span class="tile-arrow"><svg width="24" height="24" viewBox="0 0 24 24" fill="none" stroke="#222" stroke-width="2.6" stroke-linecap="round" stroke-linejoin="round"><path d="M4 12h16M13 5l7 7-7 7"/></svg></span>
</a>
<a class="tile" href="#" style="left:784px">
  <p class="tile-text">Sed ut perspiciatis<br>unde sit voluptatem<br>kolu bjuzs</p>
  <div class="tile-title">SPER</div>
  <div class="tile-art" role="img" aria-label="Lying cat photo" style="background:linear-gradient(160deg,#4a4440,#8a7e74 45%,#efeae4)"></div>
  <span class="tile-arrow"><svg width="24" height="24" viewBox="0 0 24 24" fill="none" stroke="#222" stroke-width="2.6" stroke-linecap="round" stroke-linejoin="round"><path d="M4 12h16M13 5l7 7-7 7"/></svg></span>
</a>

<h2 class="section-title" style="top:2088px">Unique Selling Points (USPs)</h2>

<div class="usp" style="left:75px">
  <div class="usp-icon"><svg width="60" height="50" viewBox="0 0 60 50" fill="none" stroke="#fff" stroke-width="3" stroke-linecap="round" stroke-linejoin="round"><path d="M14 8h26v26H14zM40 16h9l7 9v9H40"/><circle cx="22" cy="38" r="5"/><circle cx="47" cy="38" r="5"/><path d="M2 16h8M4 24h8"/></svg></div>
  <h3 class="usp-title">fast delivery</h3>
  <p class="usp-text">Lorem ipsum dolor sit amet,<br>consectetur adipiscing elit, sed<br>do eiusmod tempor et dolore.</p>
</div>
<div class="usp" style="left:439px">
  <div class="usp-icon"><svg width="56" height="56" viewBox="0 0 56 56" fill="none" stroke="#fff" stroke-width="3" stroke-linecap="round" stroke-linejoin="round"><circle cx="24" cy="16" r="9"/><path d="M6 48c0-10 8-16 18-16"/><path d="M38 32l10 4v7c0 5-5 8-10 10-5-2-10-5-10-10v-7z"/></svg></div>
  <h3 class="usp-title">Trusted by professionals</h3>
  <p class="usp-text">Lorem ipsum dolor sit amet,<br>consectetur adipiscing elit, sed<br>do eiusmod tempor et dolore.</p>
</div>
<div class="usp" style="left:787px">
  <div class="usp-icon"><svg width="58" height="58" viewBox="0 0 58 58" fill="none" stroke="#fff" stroke-width="3" stroke-linecap="round" stroke-linejoin="round"><path d="M29 4l5 10 11 2-8 8 2 11-10-5-10 5 2-11-8-8 11-2z"/><path d="M8 34l21 10 21-10v10L29 54 8 44z"/></svg></div>
  <h3 class="usp-title">High-quality feed</h3>
  <p class="usp-text">Lorem ipsum dolor sit amet,<br>consectetur adipiscing elit, sed<br>do eiusmod tempor et dolore.</p>
</div>

<h2 class="seo-title">Exercitation ullamco laboris</h2>
<p class="seo-text">Lorem ipsum dolor sit amet, consectetur adipiscing elit, sed do eiusmod tempor incididunt ut labore et dolore magna aliqua. Ut enim ad minim veniam, quis nostrud exercitation ullamco laboris nisi ut aliquip ex ea commodo consequat. Duis aute irure dolor in reprehenderit in voluptate velit esse cillum dolore eu fugiat nulla pariatur. Excepteur sint occaecat cupidatat non proident, sunt in culpa qui officia deserunt mollit anim id est laborum.</p>
<div class="divider"></div>

<form>
  <div class="field" style="left:95px;top:2920px"><label>Lorem ipsum&nbsp; elit adipiscing</label><div class="input"></div></div>
  <div class="field" style="left:95px;top:3014px"><label>Lorem ipsum elit</label><div class="input"></div></div>
  <div class="field" style="left:95px;top:3108px"><label>Lorem ipsum knue</label><div class="input"></div></div>
  <div class="field" style="left:95px;top:3202px"><label>Lorem ipsum</label><div class="input"></div></div>
  <div class="field" style="left:95px;top:3296px"><label>Lorem ipsum</label><div class="input"></div></div>
  <div class="field" style="left:95px;top:3390px"><label>Lorem ipsum</label><div class="input"></div></div>

  <div class="field" style="left:683px;top:2918px"><label>Elitjjb</label><div class="input"></div></div>
  <div class="field" style="left:683px;top:3012px"><label>Lorem</label><div class="input"></div></div>
  <div class="field" style="left:683px;top:3106px"><label>Lorem ipsum knue</label><div class="input"></div></div>
  <div class="field" style="left:683px;top:3200px"><label>Ipsum</label><div class="input"></div></div>
  <div class="field" style="left:683px;top:3294px"><label>Lorem ipsum</label><div class="input"></div></div>
  <div class="submit-btn">BILL &amp; SHIP TO ADDRESS</div>
</form>

<footer class="site-footer">
  <div class="footer-col" style="left:118px"><h4>Diensten</h4><ul><li>Lorem</li><li>ipsum</li><li>dolor sit</li><li>amet</li><li>consectetur</li><li>adipiscing</li><li>eiusmod</li><li>tempor</li></ul></div>
  <div class="footer-col" style="left:356px"><h4>Discover</h4><ul><li>Lorem</li><li>ipsum</li><li>dolor sit</li><li>amet</li><li>consectetur</li><li>adipiscing</li><li>eiusmod</li><li>tempor</li></ul></div>
  <div class="footer-col" style="left:596px"><h4>Get in touch</h4><ul><li>Lorem</li><li>ipsum</li><li>dolor sit</li><li>amet</li><li>consectetur</li><li>adipiscing</li><li>eiusmod</li><li>tempor</li></ul></div>
  <div class="footer-brand"><span class="brand-dot"></span><span class="brand-name">Brenvik</span></div>
  <a class="chat" href="#" aria-label="Chat">
    <svg width="44" height="44" viewBox="0 0 24 24" fill="none" stroke="#fff" stroke-width="2" stroke-linecap="round" stroke-linejoin="round"><path d="M22 16.9v3a2 2 0 0 1-2.2 2 19.8 19.8 0 0 1-8.6-3.1 19.5 19.5 0 0 1-6-6A19.8 19.8 0 0 1 2.1 4.2 2 2 0 0 1 4.1 2h3a2 2 0 0 1 2 1.7c.1.9.4 1.8.7 2.7a2 2 0 0 1-.5 2.1L8 9.8a16 16 0 0 0 6 6l1.3-1.3a2 2 0 0 1 2.1-.4c.9.3 1.8.6 2.7.7a2 2 0 0 1 1.7 2z"/></svg>
  </a>
  <span class="chat-badge">1</span>
  <p class="chat-label">Let’s<br>have<br>a chat !</p>
</footer>

</body>
</html>
```